New business card design needed for Diesel Fitting (Mechanical) Company

We need a new business card for our company called "Gumtree Engine Works" that showcases our logo and business details.
Target Market(s)
Owners of all makes and models of vehicles, trucks, plant and machinery.
Industry/Entity Type
Mechanical
Contact Information for Business Card
The business card details need to include the following: Owners/Directors: Doug & Marisol Brent-Coyle ABN: 41 917 302 846 Address: 317 Wattlebrook Street BRIGALOW DOWNS QLD 4899 Postal Address: PO Box 5791 BRIGALOW DOWNS QLD 4899 Website: www.gewservice.com.au Phone: 4712 9083 Mobile: 0438 175 906 Emails: sales@gewservice.com.au; admin@gewservice.com.au; accounts@gewservice.com.au; parts@gewservice.com.au; office@gewservice.com.au, reception@gewservice.com.au
Look and feel

```html
<!DOCTYPE html>
<html lang="en">
<head>
<meta charset="utf-8">
<title>Gumtree Engine Works – Business Card</title>
<link href="https://fonts.googleapis.com/css2?family=Arimo:wght@400&family=Questrial&display=swap" rel="stylesheet">
<style>
  :root {
    --backdrop: #e9e6e4;
    --card: #f7f5f4;
    --ink: #000000;
    --paper-text: #ffffff;
    --orange: #f47a20;
    --red: #e4202a;
    --gold: #f5b40f;
    --muted: #9a9a9a;
  }
  * { box-sizing: border-box; margin: 0; padding: 0; }
  html, body { width: 1200px; height: 1181px; overflow: hidden; }
  body {
    background: var(--backdrop);
    font-family: "Arimo", Arial, sans-serif;
    position: relative;
  }
  .card {
    position: absolute;
    width: 655px;
    height: 404px;
    background: var(--card);
    overflow: hidden;
    box-shadow: 0 6px 20px rgba(0,0,0,0.12);
  }
  .card-front { left: 180px; top: 156px; }
  .card-back { left: 480px; top: 627px; }
  .card-shape { position: absolute; inset: 0; }

  .contact-line {
    position: absolute;
    left: 30px;
    display: flex;
    align-items: center;
    gap: 8px;
    color: var(--paper-text);
    font-size: 18.5px;
    line-height: 1;
    white-space: nowrap;
  }
  .contact-line svg { width: 17px; height: 17px; flex: none; }
  .accent { color: var(--orange); }

  .owner-name {
    position: absolute;
    left: 30px; top: 306px;
    font-family: "Questrial", sans-serif;
    font-size: 23px;
    color: var(--orange);
    white-space: nowrap;
  }
  .owner-role {
    position: absolute;
    left: 30px; top: 334px;
    font-size: 18px;
    color: var(--paper-text);
  }

  .brand {
    position: absolute;
    font-family: "Questrial", sans-serif;
    text-align: center;
    line-height: 1.1;
  }
  .brand-front {
    left: 378px; top: 128px; width: 250px;
    font-size: 34px;
    color: var(--orange);
  }
  .brand-mark {
    width: 22px; height: 22px; border-radius: 50%;
    background: var(--orange);
    margin: 0 auto 12px;
  }
  .brand-faint {
    left: 20px; top: 150px; width: 260px;
    font-size: 34px;
    color: var(--muted);
    opacity: 0.45;
  }

  .address-block {
    position: absolute;
    right: 63px;
    color: var(--paper-text);
    font-size: 18.5px;
    line-height: 23.5px;
    text-align: right;
    white-space: nowrap;
  }
  .address-street { top: 140px; }
  .address-postal { top: 247px; }
  .pin {
    position: absolute;
    right: 36px;
    width: 17px; height: 24px;
  }
  .pin-street { top: 144px; }
  .pin-postal { top: 250px; }
</style>
</head>
<body>

<section class="card card-front">
  <svg class="card-shape" viewBox="0 0 655 404" aria-hidden="true">
    <path d="M0,0 H199 C300,60 372,200 366,322 L455,404 H0 Z" fill="var(--ink)"/>
    <path d="M199,0 C300,60 372,200 366,322 L455,404" fill="none" stroke="var(--red)" stroke-width="4"/>
  </svg>

  <div class="contact-line" style="top:48px">
    <svg viewBox="0 0 24 24"><path d="M6.6 10.8a15 15 0 0 0 6.6 6.6l2.2-2.2a1 1 0 0 1 1-.25 11.4 11.4 0 0 0 3.6.6 1 1 0 0 1 1 1V20a1 1 0 0 1-1 1A17 17 0 0 1 3 4a1 1 0 0 1 1-1h3.5a1 1 0 0 1 1 1c0 1.250.2 2.450.57 3.57a1 1 0 0 1-.25 1z" fill="var(--orange)"/></svg>
    <span>4712 9083</span>
  </div>
  <div class="contact-line" style="top:72px">
    <svg viewBox="0 0 24 24"><rect x="6" y="2" width="12" height="20" rx="2" fill="none" stroke="var(--orange)" stroke-width="2"/><circle cx="12" cy="18" r="1.2" fill="var(--orange)"/></svg>
    <span>0438 175 906</span>
  </div>
  <div class="contact-line" style="top:97px">
    <svg viewBox="0 0 24 24"><g fill="none" stroke="var(--orange)" stroke-width="1.8"><circle cx="12" cy="12" r="9"/><ellipse cx="12" cy="12" rx="4" ry="9"/><path d="M3 12h18M5 7h14M5 17h14"/></g></svg>
    <span>www.<span class="accent">gewservice</span>.com.au</span>
  </div>

  <div class="contact-line" style="top:138px"><svg viewBox="0 0 24 24"><rect x="2" y="5" width="20" height="14" fill="var(--orange)"/><path d="M2 5l10 8 10-8M2 19l7-7M22 19l-7-7" fill="none" stroke="var(--ink)" stroke-width="1.4"/></svg><span>sales@gewservice.com.au</span></div>
  <div class="contact-line" style="top:161px"><svg viewBox="0 0 24 24"><rect x="2" y="5" width="20" height="14" fill="var(--orange)"/><path d="M2 5l10 8 10-8M2 19l7-7M22 19l-7-7" fill="none" stroke="var(--ink)" stroke-width="1.4"/></svg><span>admin@gewservice.com.au</span></div>
  <div class="contact-line" style="top:185px"><svg viewBox="0 0 24 24"><rect x="2" y="5" width="20" height="14" fill="var(--orange)"/><path d="M2 5l10 8 10-8M2 19l7-7M22 19l-7-7" fill="none" stroke="var(--ink)" stroke-width="1.4"/></svg><span>accounts@gewservice.com.au</span></div>
  <div class="contact-line" style="top:208px"><svg viewBox="0 0 24 24"><rect x="2" y="5" width="20" height="14" fill="var(--orange)"/><path d="M2 5l10 8 10-8M2 19l7-7M22 19l-7-7" fill="none" stroke="var(--ink)" stroke-width="1.4"/></svg><span>parts@gewservice.com.au</span></div>
  <div class="contact-line" style="top:232px"><svg viewBox="0 0 24 24"><rect x="2" y="5" width="20" height="14" fill="var(--orange)"/><path d="M2 5l10 8 10-8M2 19l7-7M22 19l-7-7" fill="none" stroke="var(--ink)" stroke-width="1.4"/></svg><span>office@gewservice.com.au</span></div>
  <div class="contact-line" style="top:255px"><svg viewBox="0 0 24 24"><rect x="2" y="5" width="20" height="14" fill="var(--orange)"/><path d="M2 5l10 8 10-8M2 19l7-7M22 19l-7-7" fill="none" stroke="var(--ink)" stroke-width="1.4"/></svg><span>reception@gewservice.com.au</span></div>

  <div class="owner-name">Doug &amp; Marisol Brent-Coyle</div>
  <div class="owner-role">Owners/Directors</div>

  <div class="brand brand-front">
    <div class="brand-mark"></div>
    Gumtree Engine Works
  </div>
</section>

<section class="card card-back">
  <svg class="card-shape" viewBox="0 0 655 404" aria-hidden="true">
    <path d="M499,0 H655 V404 H237 L316,332 C310,200 380,70 499,0 Z" fill="var(--ink)"/>
    <path d="M499,0 C380,70 310,200 316,332 L237,404" fill="none" stroke="var(--gold)" stroke-width="4"/>
  </svg>

  <div class="brand brand-faint">Gumtree Engine Works</div>

  <div class="address-block address-street">
    <span class="accent">Address:</span> 317 Wattlebrook<br>Street BRIGALOW<br>DOWNS QLD 4899
  </div>
  <svg class="pin pin-street" viewBox="0 0 24 34" aria-hidden="true"><path d="M12 0a12 12 0 0 0-12 12c0 9 12 22 12 22s12-13 12-22A12 12 0 0 0 12 0z" fill="var(--orange)"/><circle cx="12" cy="12" r="4.5" fill="var(--ink)"/></svg>

  <div class="address-block address-postal">
    <span class="accent">Postal Address:</span> PO Box<br>5791 BRIGALOW<br>DOWNS QLD 4899
  </div>
  <svg class="pin pin-postal" viewBox="0 0 24 34" aria-hidden="true"><path d="M12 0a12 12 0 0 0-12 12c0 9 12 22 12 22s12-13 12-22A12 12 0 0 0 12 0z" fill="var(--orange)"/><circle cx="12" cy="12" r="4.5" fill="var(--ink)"/></svg>
</section>

</body>
</html>
```